Interior Decoration and Concept Store needs a webpage design

Sophisticated website for my business, name Fern Hollow. Fern Hollow is a design service and homewares store run by interior decorator Marion Tolley.

Marion's qualification and work experience as an interior decorator, is able to provide advice and recommendations for interior and exterior concepts, colour consultations, furniture, lighting, decor concepts and products are sourced for individual projects. A re-upholstery service is also provided.

Facebook icon.
Projects page.
Profile page.
Established 2009
Medial page

```html
<!DOCTYPE html>
<html lang="en">
<head>
<meta charset="utf-8">
<title>Fern Hollow — Projects</title>
<link rel="stylesheet" href="https://fonts.googleapis.com/css2?family=Arimo:ital,wght@0,400;0,700;1,400&family=Cormorant+Garamond:wght@300&display=swap">
<style>
  :root {
    --ink: #1c1c1c;
    --muted: #6b6b6b;
    --rule: #9a9a9a;
    --rule-soft: #d2d2d2;
    --button: #b3b3b3;
    --button-text: #ffffff;
    --paper: #ffffff;
    --icon: #c4c4c4;
  }
  * { box-sizing: border-box; margin: 0; padding: 0; }
  html, body { width: 1200px; height: 901px; overflow: hidden; background: var(--paper); }
  body { font-family: "Arimo", Arial, sans-serif; color: var(--ink); }
  .page { position: relative; width: 1200px; height: 901px; overflow: hidden; }

  .site-header { position: absolute; left: 111px; top: 0; width: 977px; height: 107px; border-bottom: 1px solid var(--rule); }
  .brand { position: absolute; left: 4px; top: 30px; display: flex; align-items: center; gap: 10px; font-size: 27px; letter-spacing: 2px; color: #4a4a4a; }
  .brand-mark { width: 14px; height: 14px; background: #8d8d8d; border-radius: 50%; }
  .main-nav { position: absolute; right: 0; top: 50px; display: flex; gap: 46px; list-style: none; font-size: 13.5px; letter-spacing: 0.6px; }
  .main-nav li { position: relative; }
  .main-nav .is-current::after { content: ""; position: absolute; left: 0; right: 0; top: 20px; height: 4px; background: var(--button); }

  .hero { position: absolute; left: 111px; top: 114px; width: 977px; height: 174px; overflow: hidden; }
  .hero-photo { position: absolute; inset: 0; background: linear-gradient(90deg, #6b4a32 0%, #a27a58 22%, #e8e6e2 38%, #2a2a2a 50%, #f0efed 62%, #f4f4f4 80%, #b9bbbd 86%, #e9e9e9 100%); }
  .hero-title { position: absolute; left: 0; bottom: -6px; font-family: "Cormorant Garamond", Georgia, serif; font-weight: 300; font-size: 60px; letter-spacing: 3px; color: #ffffff; line-height: 1; }
  .hero-rule { position: absolute; left: 111px; top: 296px; width: 977px; border-top: 1px solid var(--rule); }

  .intro { position: absolute; left: 111px; top: 317px; width: 977px; font-size: 13.5px; line-height: 19px; letter-spacing: 0.5px; }

  .project-grid { position: absolute; left: 111px; top: 378px; width: 977px; display: grid; grid-template-columns: repeat(3, 315px); column-gap: 16px; row-gap: 5px; }
  .project-card { border-top: 2px solid var(--rule-soft); border-bottom: 1px solid var(--rule); height: 228px; position: relative; }
  .project-photo { margin-top: 2px; height: 176px; }
  .project-title { position: absolute; left: 1px; top: 191px; font-size: 13.5px; font-weight: 400; letter-spacing: 0.5px; }
  .project-date { position: absolute; left: 1px; top: 209px; font-size: 11px; font-style: italic; letter-spacing: 0.4px; }
  .read-more { position: absolute; right: 0; top: 193px; width: 77px; height: 23px; background: var(--button); color: var(--button-text); font-size: 9.5px; letter-spacing: 0.6px; display: flex; align-items: center; justify-content: center; text-decoration: none; }

  .tone-lounge { background: linear-gradient(135deg, #3a3a38 0%, #cfc7bc 45%, #a39c93 75%, #e9e7e3 100%); }
  .tone-living { background: linear-gradient(135deg, #ddd3c9 0%, #a8a198 45%, #6b4a35 75%, #2a2522 100%); }
  .tone-console { background: linear-gradient(180deg, #f3f3f3 0%, #ececec 55%, #1f8e86 75%, #e9e9e9 100%); }
  .tone-bedroom { background: linear-gradient(135deg, #f1efec 0%, #c8c0b6 50%, #8a8179 80%, #bdb5ab 100%); }
  .tone-dining { background: linear-gradient(135deg, #f2f2f2 0%, #d45a1c 30%, #8e6a4c 55%, #2a2a2a 70%, #b7b9bb 100%); }
  .tone-study { background: linear-gradient(135deg, #b68a5e 0%, #e8e3dc 40%, #3d3d3d 60%, #d7c6a6 85%, #efefef 100%); }

  .site-footer { position: absolute; left: 111px; top: 851px; width: 977px; border-top: 1px solid var(--rule); padding-top: 10px; font-size: 10.5px; letter-spacing: 0.3px; }
  .contact-line span { margin-right: 14px; }
  .contact-line b { font-weight: 700; margin-right: 3px; }
  .copyright { font-style: italic; margin-top: 2px; }
  .social { position: absolute; right: 0; top: 13px; display: flex; gap: 5px; list-style: none; }
  .social li { width: 23px; height: 23px; background: var(--icon); }
</style>
</head>
<body>
<div class="page">
  <header class="site-header">
    <div class="brand"><span>Fern Hollow</span><span class="brand-mark"></span></div>
    <ul class="main-nav">
      <li class="is-current">HOME</li>
      <li>ABOUT US</li>
      <li>PROJECTS</li>
      <li>MEDIA</li>
      <li>CONTACT US</li>
    </ul>
  </header>

  <section class="hero">
    <div class="hero-photo" role="img" aria-label="Dining room with a timber table, orange glass vase and black chairs"></div>
    <h1 class="hero-title">PROJECTS</h1>
  </section>
  <div class="hero-rule"></div>

  <p class="intro">Inspiration is drawn from passion for quality products... the homewares range is stylish and consists of unique furniture pieces, decor accessories and lighting.</p>

  <main class="project-grid">
    <article class="project-card">
      <div class="project-photo tone-lounge" role="img" aria-label="Lounge armchair with a striped throw and cushion"></div>
      <h2 class="project-title">PROJECT ONE</h2>
      <p class="project-date">January 2014</p>
      <a class="read-more" href="#">READ MORE</a>
    </article>
    <article class="project-card">
      <div class="project-photo tone-living" role="img" aria-label="Living room with a sofa, side table and billiard table"></div>
      <h2 class="project-title">PROJECT TWO</h2>
      <p class="project-date">January 2014</p>
      <a class="read-more" href="#">READ MORE</a>
    </article>
    <article class="project-card">
      <div class="project-photo tone-console" role="img" aria-label="Teal campaign chest beneath framed artwork"></div>
      <h2 class="project-title">PROJECT THREE</h2>
      <p class="project-date">January 2014</p>
      <a class="read-more" href="#">READ MORE</a>
    </article>
    <article class="project-card">
      <div class="project-photo tone-bedroom" role="img" aria-label="Bedroom with linen bedding and a bedside lamp"></div>
      <h2 class="project-title">PROJECT FOUR</h2>
      <p class="project-date">January 2014</p>
      <a class="read-more" href="#">READ MORE</a>
    </article>
    <article class="project-card">
      <div class="project-photo tone-dining" role="img" aria-label="Dining table with an orange vase and black chairs"></div>
      <h2 class="project-title">PROJECT FIVE</h2>
      <p class="project-date">January 2014</p>
      <a class="read-more" href="#">READ MORE</a>
    </article>
    <article class="project-card">
      <div class="project-photo tone-study" role="img" aria-label="Study nook with a desk, timber chair and patterned cushion"></div>
      <h2 class="project-title">PROJECT SIX</h2>
      <p class="project-date">January 2014</p>
      <a class="read-more" href="#">READ MORE</a>
    </article>
  </main>

  <footer class="site-footer">
    <p class="contact-line">
      <span><b>Tel</b> 03 5470 2816</span>
      <span><b>Email</b> info@fernhollow.com.au</span>
      <span><b>Address</b> 4/27 Larchmont Arcade, Larchmont Street, Westbury 3295</span>
    </p>
    <p class="copyright">Copyright Fern Hollow 2014</p>
    <ul class="social" aria-label="Social links">
      <li aria-label="Social link one"></li>
      <li aria-label="Social link two"></li>
      <li aria-label="Social link three"></li>
    </ul>
  </footer>
</div>
</body>
</html>
```